KRV Business Cards

We are a local commercial development company based in Silicon Valley and we would like a new business card. I've attached a copy of our company brochure to give a flavor of what we do, our logo, info company colors/graphics, and our current business card. We don't necessarily need a crazy makeover, but would like something that feels a little bit more "fresh" and modern (we've had the same business card design for 15+ years), but still in keeping with our overall brand -- clean, high-quality, modern but timeless. Would like to add our website to the info on the card (www.velmara.com) and would like the flexibility for some folks to have an efax number listed and some not to have that included (without it looking like there is a hole).

```html
<!DOCTYPE html>
<html lang="en">
<head>
<meta charset="utf-8">
<title>Velmara Development Company – Business Cards</title>
<link rel="stylesheet" href="https://fonts.googleapis.com/css2?family=Cinzel:wght@400;600&family=Tinos:ital,wght@0,400;1,400;1,700&display=swap">
<style>
  :root {
    --slate: #435a73;
    --paper: #ffffff;
    --backdrop: #e7e4df;
    --ink: #3f5670;
    --ink-soft: #4b5f75;
  }
  * { margin: 0; padding: 0; box-sizing: border-box; }
  html, body { width: 1200px; height: 1200px; overflow: hidden; }
  body { background: var(--backdrop); position: relative; }

  .card { position: absolute; box-shadow: 0 4px 14px rgba(0,0,0,0.18); }

  .card-front { left: 217px; top: 130px; width: 749px; height: 428px; background: var(--paper); }
  .card-front .brand-panel { position: absolute; left: 0; top: 0; width: 412px; height: 100%; background: var(--slate); }

  .company-name {
    position: absolute; color: var(--paper);
    font-family: "Cinzel", serif; font-weight: 400; white-space: nowrap;
  }
  .company-name .suffix { text-transform: lowercase; }
  .card-front .company-name { left: 38px; top: 70px; font-size: 40px; line-height: 47px; letter-spacing: 0.5px; }

  .person { position: absolute; left: 439px; top: 88px; color: var(--ink); }
  .person-name { font-family: "Cinzel", serif; font-weight: 600; font-size: 28px; line-height: 30px; letter-spacing: 0.3px; white-space: nowrap; }
  .person-title { font-family: "Tinos", serif; font-style: italic; font-size: 21px; line-height: 22px; }

  .contact { position: absolute; left: 439px; top: 238px; font-family: "Tinos", serif; font-size: 18px; color: var(--ink-soft); border-collapse: collapse; }
  .contact th { font-style: italic; font-weight: 700; text-align: left; vertical-align: top; width: 72px; color: var(--ink); padding: 0; }
  .contact td { padding: 0; white-space: nowrap; }
  .contact tr.row-address td, .contact tr.row-address th { line-height: 21px; padding-bottom: 7px; }
  .contact tr.row td, .contact tr.row th { line-height: 29.5px; }

  .card-back { left: 216px; top: 628px; width: 762px; height: 436px; background: var(--slate); }
  .card-back .company-name { left: 60px; top: 110px; font-size: 56px; line-height: 65px; letter-spacing: 0.8px; }
  .website {
    position: absolute; left: 0; right: 0; top: 400px; text-align: center;
    font-family: "Cinzel", serif; font-weight: 600; font-size: 15px; letter-spacing: 0.4px; color: var(--paper);
  }
</style>
</head>
<body>
  <section class="card card-front">
    <div class="brand-panel">
      <div class="company-name">VELMARA<br>DEVELOPMENT<br>COMPANY, <span class="suffix">llc</span></div>
    </div>
    <div class="person">
      <div class="person-name">Nora J. Halden</div>
      <div class="person-title">partner</div>
    </div>
    <table class="contact">
      <tr class="row-address"><th>address.</th><td>312 Larkspur Lane,<br>Menlo Park, California 94025</td></tr>
      <tr class="row"><th>email.</th><td>nora@velmara.com</td></tr>
      <tr class="row"><th>direct.</th><td>555.214.0386</td></tr>
      <tr class="row"><th>main.</th><td>555.214.0100</td></tr>
      <tr class="row"><th>fax.</th><td>555.467.2290</td></tr>
    </table>
  </section>

  <section class="card card-back">
    <div class="company-name">VELMARA<br>DEVELOPMENT<br>COMPANY, <span class="suffix">llc</span></div>
    <div class="website">WWW.VELMARA.COM</div>
  </section>
</body>
</html>
```